"Copper Meadow" red wine label design

We are a Sydney based company. We need to design a wine label for a Australian red wine.
Front label include following info:
Our brand: "Copper Meadow";
Product name: "Shiraz 2016";
In the bottom with small font: "Wine of Australia", "750ml"
Back label:
the back label would need to be consistent with the front label, with space for one paragraph of tasting notes, and ingredient info etc.
we would like to use white, gold and blue in this label. It should make customer feel the magical and beautiful moment of starry night.

We also need a logo design for the wine brand: "Copper Meadow"

I have attached a few wine bottle that used blue to give you some inspirations.

We need the design in AI file format.

Target Market(s)

both men and women

Industry/Entity Type

It Company

Logo Text

Copper Meadow

Requirements
Nice to have
• gold borderline, words; use of blue and white

```html
<!DOCTYPE html>
<html lang="en">
<head>
<meta charset="utf-8">
<title>Copper Meadow – Shiraz 2016 Label</title>
<link rel="stylesheet" href="https://fonts.googleapis.com/css2?family=Allura&family=Raleway:wght@400;500&display=swap">
<style>
  :root {
    --backdrop: #b9b1ad;
    --paper: #ffffff;
    --navy: #0c2259;
    --navy-deep: #071840;
    --ink-blue: #1c3a8c;
    --gold: #d4b04a;
    --gold-light: #f2dc8a;
    --gold-dark: #a9832a;
    --sky-light: #2a8fd0;
    --sky-mid: #135aa8;
  }
  html, body {
    margin: 0;
    padding: 0;
    width: 1199px;
    height: 1200px;
    overflow: hidden;
    background: var(--backdrop);
  }
  .canvas {
    position: relative;
    width: 1199px;
    height: 1200px;
    display: flex;
    align-items: center;
    justify-content: center;
  }
  .label {
    position: relative;
    width: 760px;
    height: 1000px;
    box-shadow: 0 12px 40px rgba(0,0,0,0.25);
    overflow: hidden;
  }
  .label-shapes {
    position: absolute;
    inset: 0;
  }
  .brand-name {
    position: absolute;
    top: 160px;
    left: 0;
    right: 0;
    margin: 0;
    text-align: center;
    font-family: "Allura", cursive;
    font-weight: 400;
    font-size: 84px;
    color: var(--ink-blue);
  }
  .sky-frame {
    position: absolute;
    top: 300px;
    left: 225px;
    width: 310px;
    height: 290px;
    padding: 10px;
    box-sizing: border-box;
    background: var(--paper);
    border: 4px solid var(--gold);
    box-shadow: 0 6px 14px rgba(0,0,0,0.35);
  }
  .sky-scene {
    width: 100%;
    height: 100%;
    background:
      linear-gradient(180deg, transparent 70%, #0a2a6e 82%, #06163c 100%),
      radial-gradient(ellipse at 60% 30%, var(--sky-light), var(--sky-mid) 70%);
  }
  .wine-name {
    position: absolute;
    top: 610px;
    left: 0;
    right: 0;
    margin: 0;
    text-align: center;
    font-family: "Allura", cursive;
    font-weight: 400;
    font-size: 112px;
    line-height: 1;
    background: linear-gradient(180deg, var(--gold-light), var(--gold) 55%, var(--gold-dark));
    -webkit-background-clip: text;
    background-clip: text;
    color: transparent;
  }
  .star-field {
    position: absolute;
    top: 740px;
    left: 0;
    width: 760px;
    height: 160px;
    background: radial-gradient(ellipse at 50% 90%, rgba(212,176,74,0.35), rgba(212,176,74,0.08) 60%, transparent 80%);
  }
  .bottom-line {
    position: absolute;
    top: 918px;
    left: 0;
    right: 0;
    margin: 0;
    text-align: center;
    font-family: "Raleway", sans-serif;
    font-weight: 500;
    font-size: 24px;
    letter-spacing: 0.5px;
    color: var(--ink-blue);
  }
  .bottom-line .divider {
    margin: 0 14px;
  }
</style>
</head>
<body>
<main class="canvas">
  <section class="label">
    <svg class="label-shapes" width="760" height="1000" viewBox="0 0 760 1000" aria-hidden="true">
      <defs>
        <linearGradient id="goldBand" x1="0" y1="0" x2="1" y2="0">
          <stop offset="0" stop-color="#a9832a"/>
          <stop offset="0.3" stop-color="#f2dc8a"/>
          <stop offset="0.6" stop-color="#d4b04a"/>
          <stop offset="1" stop-color="#a9832a"/>
        </linearGradient>
        <linearGradient id="navyFill" x1="0" y1="0" x2="0" y2="1">
          <stop offset="0" stop-color="#071840"/>
          <stop offset="0.5" stop-color="#0c2259"/>
          <stop offset="1" stop-color="#102a6a"/>
        </linearGradient>
      </defs>
      <rect class="paper" width="760" height="1000" fill="#ffffff"/>
      <path class="night-panel" d="M0,470 Q380,420 760,480 L760,1000 L0,1000 Z" fill="url(#navyFill)"/>
      <path class="gold-edge" d="M0,470 Q380,420 760,480" fill="none" stroke="url(#goldBand)" stroke-width="6"/>
      <path class="gold-band" d="M0,900 Q380,880 760,905 L760,965 Q380,940 0,960 Z" fill="url(#goldBand)"/>
    </svg>

    <h1 class="brand-name">Copper Meadow</h1>

    <div class="sky-frame">
      <div class="sky-scene" role="img" aria-label="Night sky full of stars above layered blue mountain ridges"></div>
    </div>

    <h2 class="wine-name">Shiraz 2016</h2>

    <div class="star-field" role="img" aria-label="Scattered small gold stars across the night-blue panel"></div>

    <p class="bottom-line">Wine of Australia<span class="divider">|</span>750ml</p>
  </section>
</main>
</body>
</html>
```